PowerPoint Design for a Biotech Consulting Firm

We need a powerpoint design for a new business based in Philadelphia called VentoraRx. This is a consulting firm that will serve medical diagnostics industry, which is part of the life science/healthcare industry focusing on developing and marketing products that help in early detection, monitoring or management of diseases. Our consulting firm will help medical diagnostic companies to overcome key challenges in designing, evaluating and marketing new products.Our company name is VentoraRx. Ventora is Latin word for "something", Dx represents diagnostics. The idea behind the name is that we help companies to transform the original, early product ideas ("nothing") into "something" which is a product with full clinical utility that will help to improve health and well-being.The powerpoint should use the visual feel of the logo (attached), be modern, simple and clean looking and represent creativity, innovation, scientific thinking and progress.

Target Market(s)

Biotech

Industry/Entity Type

Biotechnology

Font styles to use
Sans Serif

Colors
0355a3
3276b5
85abd2
cfdeed
ffffff
959595
aaaaaa
cbcbcb
070707

Requirements
Must have
• - look and feel, logo colors
• - multiple slide formats

```html
<!DOCTYPE html>
<html lang="en">
<head>
<meta charset="UTF-8">
<title>VentoraRx – Contents</title>
<link rel="stylesheet" href="https://fonts.googleapis.com/css2?family=Arimo:wght@400;500;700&display=swap">
<style>
  :root {
    --brand-blue: #0355a3;
    --mid-blue: #3276b5;
    --light-blue: #85abd2;
    --pale-blue: #cfdeed;
    --white: #ffffff;
    --rule-grey: #959595;
    --ink: #070707;
    --text: #222222;
  }
  * { margin: 0; padding: 0; box-sizing: border-box; }
  html, body { width: 1200px; height: 675px; overflow: hidden; background: var(--white); }
  body { font-family: "Arimo", Arial, sans-serif; }

  .slide { position: relative; width: 1200px; height: 675px; overflow: hidden; background: var(--white); }

  .side-bar {
    position: absolute; left: 0; top: 0; width: 42px; height: 675px;
    background: var(--brand-blue);
    box-shadow: 3px 0 5px rgba(0,0,0,0.18);
  }

  .slide-title {
    position: absolute; left: 136px; top: 58px;
    font-size: 53px; font-weight: 400; color: var(--brand-blue); letter-spacing: -0.5px;
  }
  .title-rule {
    position: absolute; left: 136px; top: 126px; width: 120px; height: 4px;
    background: var(--rule-grey);
  }

  .contents-list { position: absolute; left: 136px; top: 145px; list-style: none; }
  .contents-item { display: flex; height: 36px; align-items: center; font-size: 19px; color: var(--text); }
  .item-number { width: 44px; color: var(--brand-blue); }

  .brand { position: absolute; left: 137px; top: 548px; }
  .brand-name { display: flex; align-items: center; gap: 10px; font-size: 25px; font-weight: 500; color: var(--ink); }
  .brand-square { width: 14px; height: 14px; background: var(--mid-blue); }
  .brand-tagline {
    margin-top: 52px; font-size: 8.5px; font-weight: 700; color: var(--ink); letter-spacing: 0.2px;
  }

  .hero-visual {
    position: absolute; left: 643px; top: 0; width: 557px; height: 675px;
    background:
      radial-gradient(circle at 78% 48%, rgba(40,150,240,0.75) 0%, rgba(10,80,170,0.45) 30%, rgba(2,30,70,0) 62%),
      linear-gradient(160deg, #021226 0%, #03346e 55%, #042a5a 100%);
  }
  .hero-accent {
    position: absolute; left: 1038px; top: 0; width: 71px; height: 101px;
    background: var(--brand-blue);
  }
</style>
</head>
<body>
<main class="slide">
  <div class="side-bar"></div>

  <h1 class="slide-title">Contents</h1>
  <div class="title-rule"></div>

  <ol class="contents-list">
    <li class="contents-item"><span class="item-number">1</span>Lorem ipsum dolor sit amet</li>
    <li class="contents-item"><span class="item-number">2</span>Consectetur adipiscing elit</li>
    <li class="contents-item"><span class="item-number">3</span>Tempor incididunt</li>
    <li class="contents-item"><span class="item-number">4</span>Exercitation ullamco</li>
    <li class="contents-item"><span class="item-number">5</span>Laboris nisi ut aliquip ex ea</li>
    <li class="contents-item"><span class="item-number">6</span>Commodo consequat</li>
  </ol>

  <div class="brand">
    <div class="brand-name"><span class="brand-square"></span>VentoraRx</div>
    <div class="brand-tagline">FROM CONCEPT TO CLINIC</div>
  </div>

  <div class="hero-visual" role="img" aria-label="Glowing blue digital illustration of hexagon medical icons connected by circuit lines"></div>
  <div class="hero-accent"></div>
</main>
</body>
</html>
```